Geschäftspapiere für Nachlassmanagement, Testamentsvollstreckung und Nachlassangelegenheiten
Zielgruppe
Nachtrag: Bitte keine Felder für Bankverbindungen. Mann arbeitet in der Branche mit verschiedenen Konten und der Briefempfänger könnte so schnell auf ein falsches Konto zahlen ;o).
Bitte nicht einfach das Logo oben rein und/oder Wasserbild. Das wäre mir persönlich zu einfach und kann ich selbst gestalten ;o). Ich suche nach etwas aussagekräftiges
Nachlassmanagement, Testamentsvollstreckung und Nachlassangelegenheiten
Aufgabenstellung
farben der Homepage sollten sich im Brief wiederspiegeln. eigenes Logo mit einbinden. Inhalt inkl. Telefon, Fax, Adresse, Email, Homepage, Steuernummer
auf der Rückseite der Visitenkarten soll von mir später noch ein QR Code rechts eingefügt werden können

```html
<!DOCTYPE html>
<html lang="de">
<head>
<meta charset="utf-8">
<title>Holm Nachlassmanagement – Briefbogen</title>
<link href="https://fonts.googleapis.com/css2?family=Open+Sans:wght@400&family=Arimo:wght@400&display=swap" rel="stylesheet">
<style>
  :root {
    --backdrop: #e4e5e6;
    --paper: #ffffff;
    --ink: #1f1f1f;
    --ink-soft: #3a3a3a;
    --band-dark: #1c1c1c;
    --band-grey: #5e5e5e;
    --fold: #b9b9b9;
    --signature: #1a2a8c;
  }
  * { box-sizing: border-box; margin: 0; padding: 0; }
  html, body { width: 1200px; height: 945px; overflow: hidden; }
  body { background: var(--backdrop); position: relative; }

  .letterhead {
    position: absolute; left: 282px; top: 22px;
    width: 636px; height: 900px;
    background: var(--paper);
    box-shadow: 0 4px 18px rgba(0,0,0,.18);
    overflow: hidden;
    color: var(--ink);
    font-family: "Open Sans", sans-serif;
  }
  .top-swoosh { position: absolute; left: 0; top: 0; }

  .brand-mark {
    position: absolute; left: 62px; top: 50px;
    width: 42px; height: 42px; border-radius: 50%;
    border: 2px solid var(--ink-soft);
  }
  .brand-name {
    position: absolute; left: 122px; top: 52px;
    font-family: "Open Sans", sans-serif; font-weight: 400;
    font-size: 26px; line-height: 32px; color: var(--ink);
  }
  .brand-tagline {
    position: absolute; left: 124px; top: 86px;
    font-family: "Open Sans", sans-serif; font-size: 11px;
    letter-spacing: 0.5px; color: var(--ink-soft);
  }

  .sender-block {
    position: absolute; left: 448px; top: 132px;
    border-left: 1px solid var(--ink-soft);
    padding-left: 10px;
    font-style: normal;
    font-size: 8px; line-height: 11.5px; color: var(--ink-soft);
  }
  .sender-block .contact { display: flex; align-items: center; gap: 5px; }
  .sender-block svg { width: 7px; height: 7px; fill: var(--ink-soft); }

  .return-line {
    position: absolute; left: 72px; top: 190px;
    font-size: 5.5px; color: var(--ink-soft);
    border-bottom: 0.8px solid var(--ink-soft); padding-bottom: 1px;
  }
  .recipient {
    position: absolute; left: 76px; top: 212px;
    font-style: normal; font-size: 9px; line-height: 12px;
  }

  .letter-body {
    position: absolute; left: 76px; top: 300px; width: 490px;
    font-family: "Arimo", sans-serif; font-size: 10px; line-height: 12.5px;
  }
  .letter-body p { margin-bottom: 13px; text-align: justify; }
  .letter-body .salutation { margin-bottom: 15px; }
  .closing { margin-top: 16px; }
  .signature-area {
    width: 190px; height: 42px; margin: 6px 0 4px -6px;
    background: linear-gradient(90deg, rgba(26,42,140,.10), rgba(26,42,140,.04));
    border-radius: 3px;
  }
  .signer { font-family: "Open Sans", sans-serif; font-size: 10px; margin-left: 30px; }

  .fold-mark {
    position: absolute; left: 0; width: 14px;
    border-top: 1px solid var(--fold);
  }
  .fold-mark.first { top: 318px; }
  .fold-mark.punch { top: 450px; }
  .fold-mark.second { top: 636px; }

  .footer-bands { position: absolute; left: 0; bottom: 0; }
  .footer-tax {
    position: absolute; left: 24px; bottom: 7px;
    font-size: 9px; line-height: 12px; color: #ffffff; letter-spacing: .2px;
  }
  .footer-web {
    position: absolute; left: 478px; bottom: 16px;
    width: 116px; text-align: center;
    font-size: 9px; line-height: 12px; color: #ffffff;
  }
</style>
</head>
<body>
  <article class="letterhead">
    <svg class="top-swoosh" width="636" height="70" viewBox="0 0 636 70" aria-hidden="true">
      <path d="M0 0 H636 V10 H150 C70 10 20 24 0 60 Z" fill="var(--band-grey)"/>
    </svg>

    <header>
      <span class="brand-mark" aria-hidden="true"></span>
      <div class="brand-name">Holm Nachlassmanagement</div>
      <div class="brand-tagline">Sorgfalt im Nachlass</div>
    </header>

    <address class="sender-block">
      <div>HOLM NACHLASSMANAGEMENT</div>
      <div>Lindenallee 27</div>
      <div>48153 Altenbrück</div>
      <div class="contact">
        <svg viewBox="0 0 10 10"><path d="M2 0.5 L3.8 2.6 L2.8 3.8 C3.4 5.3 4.7 6.6 6.2 7.2 L7.4 6.2 L9.5 8 L8.3 9.5 C4.5 9.3 0.7 5.5 0.5 1.7 Z"/></svg>
        <span>+49 (0) 4821 / 55 20 130</span>
      </div>
      <div class="contact">
        <svg viewBox="0 0 10 10"><rect x="2" y="0.5" width="6" height="3"/><rect x="0.5" y="3.5" width="9" height="4.5" rx="1"/><rect x="2" y="7" width="6" height="2.5"/></svg>
        <span>+49 (0) 4821 / 55 20 131</span>
      </div>
      <div class="contact">
        <svg viewBox="0 0 10 10"><path d="M0.5 2 H9.5 V8 H0.5 Z M0.5 2 L5 5.5 L9.5 2" fill="none" stroke="var(--ink-soft)" stroke-width="1"/></svg>
        <span>info@nachlass-holm.de</span>
      </div>
    </address>

    <div class="return-line">HOLM NACHLASSMANAGEMENT | Lindenallee 27 | 48153 Altenbrück</div>

    <address class="recipient">
      Herr<br>Mark Mustermann<br>Musterweg 13<br>24102 Musterstadtstadt
    </address>

    <span class="fold-mark first"></span>
    <span class="fold-mark punch"></span>
    <span class="fold-mark second"></span>

    <section class="letter-body">
      <p class="salutation">Sehr geehrte Damen und Herren,</p>
      <p>Lorem ipsum dolor sit amet, consectetur adipiscing elit. Proin tincidunt, lectus id malesuada cursus, lorem augue egestas magna, ut mattis orci ante ut arcu. Sed mauris tellus, fermentum quis ligula nec, posuere pulvinar eros. Nam at mi quis velit pellentesque finibus. Donec lacus velit, faucibus mollis dolor nec, finibus pellentesque orci. Duis sed dictum elit, ut posuere arcu.</p>
      <p>Sed pretium ac enim eu viverra. Aliquam ac est eget magna convallis convallis. Aenean augue purus, finibus eget turpis quis, finibus dignissim nibh. Phasellus viverra lobortis dignissim. Duis varius turpis in sapien accumsan facilisis. Sed vehicula gravida diam a interdum. Nullam convallis ligula id erat egestas consequat. Integer consectetur ex vel aliquet iaculis. Vestibulum molestie.</p>
      <p class="closing">Mit freundlichen Grüßen</p>
      <div class="signature-area" role="img" aria-label="Handschriftliche Unterschrift in blauer Tinte"></div>
      <p class="signer">Greta Holmberg</p>
    </section>

    <svg class="footer-bands" width="636" height="60" viewBox="0 0 636 60" aria-hidden="true">
      <path d="M0 34 H470 L458 60 H0 Z" fill="var(--band-dark)"/>
      <path d="M0 56 H636 V60 H0 Z" fill="var(--band-dark)"/>
      <path d="M480 20 H604 L592 56 H466 Z" fill="var(--band-grey)"/>
      <path d="M612 20 H636 V56 H600 Z" fill="var(--band-dark)"/>
    </svg>
    <div class="footer-tax">Steuernummer: 204/317/00000 • Umsatzsteuer IDNr.: DE517204638</div>
    <div class="footer-web">www.nachlass-holm.de</div>
  </article>
</body>
</html>
```